International gym review site. Needs a full website frontend (mobile + desktop) designing and a logo

Our UK based business 'LiftHarbor' is launching its international review website for independent and hotel gyms. Our website will be a fresh, funky and clean version of Wanderquill but for gyms.
We require the designs in sketch, psd, illustrator

We would like to see clean designs that incorporate gym style icons. We also require our logo designing which will need to complement the design of the site. We have included wireframes of how we envisage the site coming together. However, we are very flexible on this and have nothing set in stone.

We would like the designs to mobile first focused with desktop experince being the latter (although we have wireframed for desktop - we are very open to ideas and suggestions)

Please find below a number of websites that we like and have found inspiration from:

- https://www.bookvane.example/uk/
- chatterloom.example
- Map is cool on here https://bigroster.bypilotcraft.example/
- Looks cool like nest n'go (listing section could be smaller) -https://tintforge.example/demos/themes/?product=rowable
- Like this but needs to be more compact https://rowkit-demos.brimfold.example/rentals/listing/private-bedroom-w-bathroom/
- Like the homepage of this one https://rankhop.venmora.example/
- https://www.paddlo.example.co.uk/hotels - looks clean, like the layout of this especially the hotel section
- https://www.paddlo.example.co.uk/Barcelona-Hotels.48213.hotel.ksp - the good to know section is good
- https://chipwire.example/2017/10/20/flickcast-unveils-a-suite-of-new-tools-to-help-creators-grow-their-channels-and-make-money/
- https://www.quietlodging.example/
- https://www.wheelmarket.example.co.uk

Target Market(s)

Fitness users and hotel goers who want to use a gym. Generally affluent aged 20-50years old of multi-nationalities

Industry/Entity Type

Fitness

Logo Text

LiftHarbor (optional)

Number of Pages Required

5+ page

Colors

Designer to choose colors to be used in the design.

Requirements
Must have
• Clean, flat minimal, pleasing on the eye.
• Bright / colourful
• Clean fonts (no specific font picked, will leave colour palette and fonts to the designer)
Should not have
• Cluttered and disorganised feel.
• Dark and dreary.

```html
<!DOCTYPE html>
<html lang="en">
<head>
<meta charset="utf-8">
<title>LiftHarbor – Barcelona</title>
<link href="https://fonts.googleapis.com/css2?family=Poppins:wght@400;500;600;700&family=Open+Sans:wght@400;600&display=swap" rel="stylesheet">
<style>
:root{
  --ink:#111;
  --text:#333;
  --muted:#555;
  --accent:#e8533a;
  --star:#f5a623;
  --band:#f0f0f0;
  --footer:#161616;
  --line:#e2e2e2;
  --bar-dark:#ee8f7a;
  --bar-light:#f8c9bd;
  --pin:#1f2a3a;
}
*{box-sizing:border-box;margin:0;padding:0}
html,body{width:1200px;height:3838px;overflow:hidden}
body{font-family:"Open Sans",sans-serif;color:var(--text);background:#fff;position:relative}
h1,h2,h3,.brand,.nav a,.btn{font-family:"Poppins",sans-serif}
.site-header{position:absolute;top:0;left:0;width:1200px;height:118px;background:#000;display:flex;align-items:center;justify-content:space-between;padding:0 97px}
.brand{display:flex;align-items:center;gap:12px;color:#fff;font-weight:700;font-size:34px;letter-spacing:-.5px}
.brand-dot{width:30px;height:30px;border-radius:50%;background:#fff}
.nav{display:flex;gap:30px}
.nav a{color:#fff;text-decoration:none;font-size:16px;font-weight:500}
.hero-map{position:absolute;top:118px;left:0;width:1200px;height:534px;background:linear-gradient(180deg,#b9d7ee 0%,#cfe3cc 28%,#dbe8cf 60%,#e7edd9 100%)}
.hero-map svg{position:absolute;left:0;top:0}
.city-card{position:absolute;left:271px;top:568px;width:658px;height:289px;background:#fff;border:1px solid var(--line);border-radius:14px;box-shadow:0 4px 14px rgba(0,0,0,.08);text-align:center;padding-top:92px}
.city-avatar{position:absolute;left:522px;top:478px;width:156px;height:156px;border-radius:50%;border:6px solid #fff;background:linear-gradient(160deg,#8fb8e4,#c9a27a);box-shadow:0 2px 8px rgba(0,0,0,.15)}
.city-card h2{font-size:22px;font-weight:500;color:var(--ink)}
.stars{color:var(--star);font-size:15px;letter-spacing:1px}
.city-card .stars{font-size:17px;margin:4px 0 14px}
.city-card p{font-size:13.5px;line-height:1.75;padding:0 80px;color:var(--muted)}
.band{position:absolute;left:0;width:1200px}
.band.grey{background:var(--band)}
.section-title{text-align:center;font-size:30px;font-weight:500;color:var(--ink)}
.card-row{position:absolute;left:97px;display:flex;gap:29px}
.card{width:317px;height:327px;background:#fff;box-shadow:0 1px 6px rgba(0,0,0,.14)}
.card-img{height:184px}
.card-body{padding:14px 14px 0}
.card-head{display:flex;justify-content:space-between;align-items:center}
.card-head h3{font-size:20px;font-weight:500;color:var(--ink)}
.card-body p{font-size:12.5px;line-height:1.75;margin-top:8px;color:var(--muted)}
.btn{position:absolute;left:542px;width:116px;height:39px;background:var(--accent);color:#fff;font-size:13px;font-weight:600;display:flex;align-items:center;justify-content:center;border-radius:3px}
.subtitle{text-align:center;font-size:14px;color:var(--muted)}
.chart{position:absolute;top:2663px;width:481px;height:343px;background:#fff;border:1px solid #d8d8d8;box-shadow:0 2px 6px rgba(0,0,0,.08)}
.chart-bar{height:16px;border-bottom:1px solid #eee;background:#fafafa}
.chart h3{font-size:15px;font-weight:600;color:#444;margin:38px 0 0 25px}
.events{position:absolute;top:3210px;left:99px;display:flex;gap:17px}
.event{width:153px}
.event-img{height:141px}
.event span{display:block;height:41px;line-height:41px;text-align:center;background:var(--band);font-size:15px;color:var(--ink)}
.site-footer{position:absolute;left:0;top:3471px;width:1200px;height:367px;background:var(--footer);color:#ddd}
.site-footer h3{font-size:19px;font-weight:600;color:#fff;letter-spacing:.5px}
.foot-col{position:absolute;top:62px}
.contact-item{display:flex;gap:14px;margin-top:18px;font-size:13px;line-height:1.6}
.contact-item svg{flex:none}
.signup p{font-size:13px;line-height:1.6;margin-top:14px;width:290px}
.signup .field{width:284px;height:41px;background:#fff;margin-top:18px;color:#888;font-size:12px;padding:12px 14px}
.signup .btn{position:static;margin-top:14px;width:112px;height:38px}
.quick a{display:block;color:#ddd;text-decoration:none;font-size:13px;margin-top:8px}
.quick h3{margin-bottom:16px}
.socials{position:absolute;left:97px;top:184px;display:flex;gap:8px}
.socials span{width:22px;height:22px;border:1.5px solid #ccc;border-radius:50%}
.copyright{position:absolute;left:0;bottom:22px;width:1200px;text-align:center;font-size:12px;color:#bbb}
</style>
</head>
<body>

<header class="site-header">
  <div class="brand"><span>LiftHarbor</span><span class="brand-dot"></span></div>
  <nav class="nav">
    <a href="#">HOME</a><a href="#">ABOUT</a><a href="#">HOTEL GYMS</a><a href="#">INDEPENDENT GYMS</a><a href="#">EVENTS</a><a href="#">CONTACT</a>
  </nav>
</header>

<section class="hero-map" role="img" aria-label="Map of the Barcelona coast with gym locations">
  <svg width="1200" height="534" viewBox="0 0 1200 534">
    <g fill="var(--pin)">
      <path d="M235 196a14 14 0 1 1 28 0c0 12-14 26-14 26s-14-14-14-26z"/>
      <path d="M422 230a14 14 0 1 1 28 0c0 12-14 26-14 26s-14-14-14-26z"/>
      <path d="M633 222a14 14 0 1 1 28 0c0 12-14 26-14 26s-14-14-14-26z"/>
      <path d="M928 166a14 14 0 1 1 28 0c0 12-14 26-14 26s-14-14-14-26z"/>
      <path d="M831 254a14 14 0 1 1 28 0c0 12-14 26-14 26s-14-14-14-26z"/>
      <path d="M145 336a14 14 0 1 1 28 0c0 12-14 26-14 26s-14-14-14-26z"/>
      <path d="M988 370a14 14 0 1 1 28 0c0 12-14 26-14 26s-14-14-14-26z"/>
    </g>
    <path d="M0 534 C300 470 520 500 700 500 C900 500 1050 480 1200 450" stroke="var(--accent)" stroke-width="5" fill="none"/>
  </svg>
</section>

<div class="city-card">
  <h2>Barcelona</h2>
  <div class="stars">★★★★★</div>
  <p>Nemo enim ipsam voluptatem quia voluptas sit aspernatur aut odit aut fugit, sed quia consetur magni dolores eos qui ratione voluptatem sequi nesciunt. Neque porro quisquam est, qui dolorem ipsum quia dolor sit amet, consectetur, adipisci velit, sed quia non</p>
</div>
<div class="city-avatar" role="img" aria-label="Barcelona landmark photo"></div>

<div class="card-row" style="top:926px">
  <article class="card"><div class="card-img" role="img" aria-label="Couple taking a selfie above the city" style="background:linear-gradient(135deg,#9cc3e6,#c99a73)"></div><div class="card-body"><div class="card-head"><h3>Barcelona</h3><span class="stars">★★★★★</span></div><p>Nemo enim ipsam voluptatem quia voluptas sit aspernatur aut odit aut fugit, sed quia constur magni dolores eos qui ratione</p></div></article>
  <article class="card"><div class="card-img" role="img" aria-label="Mosaic park terrace with city view" style="background:linear-gradient(135deg,#8db7dc,#b99256)"></div><div class="card-body"><div class="card-head"><h3>Barcelona</h3><span class="stars">★★★★★</span></div><p>Nemo enim ipsam voluptatem quia voluptas sit aspernatur aut odit aut fugit, sed quia constur magni dolores eos qui ratione</p></div></article>
  <article class="card"><div class="card-img" role="img" aria-label="Flower stall in a busy street market" style="background:linear-gradient(135deg,#b3413f,#d9b44a)"></div><div class="card-body"><div class="card-head"><h3>Barcelona</h3><span class="stars">★★★★★</span></div><p>Nemo enim ipsam voluptatem quia voluptas sit aspernatur aut odit aut fugit, sed quia constur magni dolores eos qui ratione</p></div></article>
</div>

<section class="band grey" style="top:1322px;height:571px">
  <h2 class="section-title" style="margin-top:42px">Hotel Gyms</h2>
</section>
<div class="card-row" style="top:1440px">
  <article class="card"><div class="card-img" role="img" aria-label="Hotel gym reception desk" style="background:linear-gradient(135deg,#6e5a48,#b48652)"></div><div class="card-body"><div class="card-head"><h3>Barcelona</h3><span class="stars">★★★★★</span></div><p>Nemo enim ipsam voluptatem quia voluptas sit aspernatur aut odit aut fugit, sed quia constur magni dolores eos qui ratione</p></div></article>
  <article class="card"><div class="card-img" role="img" aria-label="Hotel gym with pool and exercise bikes" style="background:linear-gradient(135deg,#5e7f8e,#a88a6a)"></div><div class="card-body"><div class="card-head"><h3>Barcelona</h3><span class="stars">★★★★★</span></div><p>Nemo enim ipsam voluptatem quia voluptas sit aspernatur aut odit aut fugit, sed quia constur magni dolores eos qui ratione</p></div></article>
  <article class="card"><div class="card-img" role="img" aria-label="Woman training in a bright hotel gym" style="background:linear-gradient(135deg,#3e3e3e,#c9a48a)"></div><div class="card-body"><div class="card-head"><h3>Barcelona</h3><span class="stars">★★★★★</span></div><p>Nemo enim ipsam voluptatem quia voluptas sit aspernatur aut odit aut fugit, sed quia constur magni dolores eos qui ratione</p></div></article>
</div>
<a class="btn" style="top:1803px">VIEW MORE</a>

<h2 class="section-title" style="position:absolute;top:1953px;width:1200px">Independent Gyms</h2>
<div class="card-row" style="top:2031px">
  <article class="card"><div class="card-img" role="img" aria-label="Spin class in a dark studio" style="background:linear-gradient(135deg,#1c1c1c,#a8643a)"></div><div class="card-body"><div class="card-head"><h3>Barcelona</h3><span class="stars">★★★★★</span></div><p>Nemo enim ipsam voluptatem quia voluptas sit aspernatur aut odit aut fugit, sed quia constur magni dolores eos qui ratione</p></div></article>
  <article class="card"><div class="card-img" role="img" aria-label="Row of treadmills in a gym" style="background:linear-gradient(135deg,#3d5d86,#a7b6c6)"></div><div class="card-body"><div class="card-head"><h3>Barcelona</h3><span class="stars">★★★★★</span></div><p>Nemo enim ipsam voluptatem quia voluptas sit aspernatur aut odit aut fugit, sed quia constur magni dolores eos qui ratione</p></div></article>
  <article class="card"><div class="card-img" role="img" aria-label="Barbell training in a gym" style="background:linear-gradient(135deg,#4a3a32,#b98a6e)"></div><div class="card-body"><div class="card-head"><h3>Barcelona</h3><span class="stars">★★★★★</span></div><p>Nemo enim ipsam voluptatem quia voluptas sit aspernatur aut odit aut fugit, sed quia constur magni dolores eos qui ratione</p></div></article>
</div>
<a class="btn" style="top:2394px">VIEW MORE</a>

<section class="band grey" style="top:2499px;height:571px">
  <h2 class="section-title" style="margin-top:48px">When To Book A Hotel Gyms In Barcelona</h2>
  <p class="subtitle" style="margin-top:8px">Price per night / 3-star Hotel Gyms. Prices are not fixed and may vary with time.</p>
</section>

<div class="chart" style="left:102px">
  <div class="chart-bar"></div>
  <h3>AVERAGE NIGHTLY PRICE PER MONTH</h3>
  <svg width="481" height="240" viewBox="0 0 481 240" font-family="Open Sans,sans-serif" font-size="10" fill="#666">
    <g stroke="#eee"><line x1="45" y1="30" x2="460" y2="30"/><line x1="45" y1="75" x2="460" y2="75"/><line x1="45" y1="120" x2="460" y2="120"/><line x1="45" y1="165" x2="460" y2="165"/><line x1="45" y1="210" x2="460" y2="210"/></g>
    <text x="15" y="34">£125</text><text x="15" y="79">£100</text><text x="20" y="124">£75</text><text x="20" y="169">£50</text><text x="26" y="214">£0</text>
    <g fill="var(--bar-dark)"><rect x="58" y="159" width="16" height="51"/><rect x="113" y="84" width="16" height="126"/><rect x="168" y="93" width="16" height="117"/><rect x="223" y="75" width="16" height="135"/><rect x="278" y="93" width="16" height="117"/><rect x="333" y="84" width="16" height="126"/><rect x="388" y="57" width="16" height="153"/></g>
    <g fill="var(--bar-light)"><rect x="76" y="147" width="16" height="63"/><rect x="131" y="80" width="16" height="130"/><rect x="186" y="156" width="16" height="54"/><rect x="241" y="84" width="16" height="126"/><rect x="296" y="174" width="16" height="36"/><rect x="351" y="159" width="16" height="51"/><rect x="406" y="150" width="16" height="60"/></g>
    <rect x="108" y="50" width="34" height="26" fill="#fff" stroke="#ccc"/><text x="114" y="61" font-size="9">Tue</text><text x="114" y="72" font-size="9">£100</text>
    <g text-anchor="middle"><text x="75" y="228">Mon</text><text x="130" y="228">Tue</text><text x="185" y="228">Wed</text><text x="240" y="228">Thu</text><text x="295" y="228">Fri</text><text x="350" y="228">Sat</text><text x="405" y="228">Sun</text></g>
  </svg>
</div>

<div class="chart" style="left:614px">
  <div class="chart-bar"></div>
  <h3>AVERAGE NIGHTLY PRICE</h3>
  <svg width="481" height="240" viewBox="0 0 481 240" font-family="Open Sans,sans-serif" font-size="10" fill="#666">
    <g stroke="#eee"><line x1="45" y1="30" x2="460" y2="30"/><line x1="45" y1="75" x2="460" y2="75"/><line x1="45" y1="120" x2="460" y2="120"/><line x1="45" y1="165" x2="460" y2="165"/><line x1="45" y1="210" x2="460" y2="210"/></g>
    <text x="15" y="34">£125</text><text x="15" y="79">£100</text><text x="20" y="124">£75</text><text x="20" y="169">£50</text><text x="26" y="214">£0</text>
    <g fill="var(--bar-dark)"><rect x="58" y="159" width="16" height="51"/><rect x="113" y="84" width="16" height="126"/><rect x="168" y="93" width="16" height="117"/><rect x="223" y="75" width="16" height="135"/><rect x="278" y="93" width="16" height="117"/><rect x="333" y="84" width="16" height="126"/><rect x="388" y="57" width="16" height="153"/></g>
    <g fill="var(--bar-light)"><rect x="76" y="147" width="16" height="63"/><rect x="131" y="80" width="16" height="130"/><rect x="186" y="156" width="16" height="54"/><rect x="241" y="84" width="16" height="126"/><rect x="296" y="174" width="16" height="36"/><rect x="351" y="159" width="16" height="51"/><rect x="406" y="150" width="16" height="60"/></g>
    <rect x="108" y="50" width="34" height="26" fill="#fff" stroke="#ccc"/><text x="114" y="61" font-size="9">Tue</text><text x="114" y="72" font-size="9">£100</text>
    <g text-anchor="middle"><text x="75" y="228">Mon</text><text x="130" y="228">Tue</text><text x="185" y="228">Wed</text><text x="240" y="228">Thu</text><text x="295" y="228">Fri</text><text x="350" y="228">Sat</text><text x="405" y="228">Sun</text></g>
  </svg>
</div>

<h2 class="section-title" style="position:absolute;top:3124px;width:1200px">Events near by</h2>
<div class="events">
  <div class="event"><div class="event-img" role="img" aria-label="Group fitness class" style="background:linear-gradient(135deg,#6a4a3c,#c88f6e)"></div><span>Event 1</span></div>
  <div class="event"><div class="event-img" role="img" aria-label="Cycling studio session" style="background:linear-gradient(135deg,#b8323a,#d9c2c0)"></div><span>Event 2</span></div>
  <div class="event"><div class="event-img" role="img" aria-label="Tall ship in the harbour" style="background:linear-gradient(135deg,#5f8fc4,#a0643c)"></div><span>Barcelona</span></div>
  <div class="event"><div class="event-img" role="img" aria-label="Couple by the sea" style="background:linear-gradient(135deg,#3f6e8c,#c79a78)"></div><span>Barcelona</span></div>
  <div class="event"><div class="event-img" role="img" aria-label="Paella dish" style="background:linear-gradient(135deg,#d28a2a,#8a5a24)"></div><span>Barcelona</span></div>
  <div class="event"><div class="event-img" role="img" aria-label="Colourful mosaic park" style="background:linear-gradient(135deg,#7aaee0,#c58a4e)"></div><span>Barcelona</span></div>
</div>

<footer class="site-footer">
  <div class="brand" style="position:absolute;left:97px;top:90px"><span>LiftHarbor</span><span class="brand-dot"></span></div>
  <div class="socials"><span></span><span></span><span></span><span></span></div>

  <div class="foot-col" style="left:335px">
    <h3>CONTACT US</h3>
    <div class="contact-item"><svg width="16" height="20" viewBox="0 0 16 20"><path d="M8 1a6 6 0 0 1 6 6c0 5-6 12-6 12S2 12 2 7a6 6 0 0 1 6-6z" fill="none" stroke="#ddd" stroke-width="1.5"/><circle cx="8" cy="7" r="2" fill="#ddd"/></svg><div>LiftHarbor<br>14 Quarry Lane Harbourside<br>Western Australia 6021</div></div>
    <div class="contact-item"><svg width="16" height="16" viewBox="0 0 16 16"><path d="M3 1l3 3-2 2c1 2 3 4 5 5l2-2 3 3-2 3C7 15 1 9 1 3z" fill="none" stroke="#ddd" stroke-width="1.4"/></svg><div>Phone: +61 08 5550 1742</div></div>
    <div class="contact-item"><svg width="16" height="14" viewBox="0 0 16 14"><rect x="1" y="2" width="14" height="10" fill="none" stroke="#ddd" stroke-width="1.4"/><path d="M1 2l7 6 7-6" fill="none" stroke="#ddd" stroke-width="1.4"/></svg><div>Email: enquiries@liftharbor.example</div></div>
  </div>

  <div class="foot-col signup" style="left:629px">
    <h3>SIGN UP TO RECEIVE EMAIL</h3>
    <p>Excepteur sint occaecat cupidatat non proident, sunt in culpa qui Nemo enim ipsam voluptatem</p>
    <div class="field">Enter email</div>
    <a class="btn">SUBSCRIBE</a>
  </div>

  <div class="foot-col quick" style="left:972px">
    <h3>QUICK LINKS</h3>
    <a href="#">HOME</a><a href="#">About</a><a href="#">Hotel Gyms</a><a href="#">Independent Gyms</a><a href="#">Events</a><a href="#">Contact</a>
  </div>

  <p class="copyright">Copyright © LiftHarbor, 2018. All rights reserved.</p>
</footer>

</body>
</html>
```